Picture storybook for a childs netball book needs a cover

We need a book cover and the pictures to go into a small picture story book which is being created for children who are learning to play netball.
It needs to be colorful and bright to appeal to young girls predominantly aged 5 - 8. It needs to include a young girl, pig tails, netball uniform, etc. The title is Poppy's sunny day at the Park
I also need some illustrations for various pages which to interested designers l will send the text.
The text will also need to be put on the pages.
Updates

The cover will move onto more work which will follow the same theme - bright animated and pictures that will capture the imagination of children

Target Market(s)

Predominantly young girls aged 5-8 and the people who will buy it for them

Industry/Entity Type

Learning

Other font styles liked:
• What the designers think will appeal to children

Colors
886aae
d3a5cc
e667a6
f04a50
fbee3e
0493ce
9bcb3c

Requirements
Must have
• A young girl who is sporty, healthy, happy little girl - she is the main character
• A whistle on every page which is hard to find but the children reading the pages will look for it in the pictures as they progress through the book
Nice to have
• Not sure at this stage
Should not have
• Not sure - nothing at this stage

```html
<!DOCTYPE html>
<html lang="en">
<head>
<meta charset="utf-8">
<title>Poppy's Sunny Day At The Park – Book Cover</title>
<link rel="stylesheet" href="https://fonts.googleapis.com/css2?family=Righteous&display=swap">
<style>
  :root {
    --page-bg: #ffffff;
    --sun-yellow: #f7e62e;
    --sun-orange: #f3a23a;
    --lime: #8cff0a;
    --lime-deep: #5fae12;
    --violet: #8060ff;
    --violet-deep: #3a2670;
    --magenta: #f24fe9;
    --lilac: #d9a6f2;
    --lilac-deep: #b78ad6;
    --photo-warm: #c88a6a;
    --photo-mid: #8a6fb0;
    --title-fill: #ffffff;
    --title-edge-a: #8a5cf0;
    --title-edge-b: #f05ad8;
  }
  html, body {
    margin: 0;
    padding: 0;
    width: 1074px;
    height: 1200px;
    overflow: hidden;
    background: var(--page-bg);
  }
  .canvas {
    position: relative;
    width: 1074px;
    height: 1200px;
  }
  .book-cover {
    position: absolute;
    left: 158px;
    top: 127px;
    width: 758px;
    height: 946px;
    display: block;
  }
  .cover-title {
    font-family: "Righteous", "Arial Rounded MT Bold", sans-serif;
    fill: var(--title-fill);
    stroke: url(#titleEdge);
    stroke-linejoin: round;
    paint-order: stroke fill;
  }
  .cover-title--name { font-size: 104px; stroke-width: 12px; }
  .cover-title--tagline { font-size: 60px; stroke-width: 10px; }
</style>
</head>
<body>
<main class="canvas">
  <svg class="book-cover" viewBox="0 0 758 946" xmlns="http://www.w3.org/2000/svg" aria-labelledby="coverTitle">
    <title id="coverTitle">Poppy's Sunny Day At The Park</title>
    <defs>
      <clipPath id="coverClip"><rect width="758" height="946"/></clipPath>
      <linearGradient id="sunWash" x1="0" y1="0" x2="1" y2="1">
        <stop offset="0" stop-color="var(--sun-yellow)"/>
        <stop offset="0.6" stop-color="var(--sun-orange)"/>
      </linearGradient>
      <radialGradient id="limeGlow" cx="0.3" cy="0.4" r="0.8">
        <stop offset="0" stop-color="var(--lime)"/>
        <stop offset="0.55" stop-color="var(--lime)"/>
        <stop offset="1" stop-color="var(--lime-deep)"/>
      </radialGradient>
      <radialGradient id="violetGlow" cx="0.3" cy="0.3" r="0.9">
        <stop offset="0" stop-color="var(--violet)"/>
        <stop offset="0.5" stop-color="#6e4fe0"/>
        <stop offset="1" stop-color="var(--violet-deep)"/>
      </radialGradient>
      <linearGradient id="lilacWash" x1="0" y1="0" x2="1" y2="1">
        <stop offset="0" stop-color="var(--lilac)"/>
        <stop offset="1" stop-color="var(--lilac-deep)"/>
      </linearGradient>
      <radialGradient id="photoTones" cx="0.5" cy="0.55" r="0.6">
        <stop offset="0" stop-color="var(--photo-mid)"/>
        <stop offset="1" stop-color="var(--photo-warm)"/>
      </radialGradient>
      <linearGradient id="titleEdge" x1="0" y1="0" x2="1" y2="0">
        <stop offset="0" stop-color="var(--title-edge-a)"/>
        <stop offset="1" stop-color="var(--title-edge-b)"/>
      </linearGradient>
    </defs>

    <g clip-path="url(#coverClip)">
      <rect class="cover-bg" width="758" height="946" fill="url(#sunWash)"/>
      <circle class="photo-window" cx="275" cy="450" r="272" fill="url(#photoTones)"
              role="img" aria-label="Photo of two young girls in netball uniforms, one holding a netball"/>
      <circle class="bubble bubble--magenta" cx="-58" cy="573" r="180" fill="var(--magenta)"/>
      <circle class="bubble bubble--lilac" cx="142" cy="923" r="290" fill="url(#lilacWash)"/>
      <circle class="bubble bubble--violet" cx="612" cy="773" r="310" fill="url(#violetGlow)"/>
      <circle class="bubble bubble--lime" cx="697" cy="233" r="325" fill="url(#limeGlow)"/>

      <text class="cover-title cover-title--name" x="52" y="660">Poppy's</text>
      <text class="cover-title cover-title--tagline" x="52" y="760" textLength="652" lengthAdjust="spacingAndGlyphs">Sunny Day At The Park</text>
    </g>
  </svg>
</main>
</body>
</html>
```